VERIDAX Need a luxury modern business card designed.

Need a luxury modern business card designed. refer to the uploaded files for the company name and logo in the zip file under source files. i will making my descion on monday. so please send in before then so if we need to edit we will have the time. we have a trade show coming up and im on a deadline for printer.

Target Market(s)

high end clients

Contact Information for Business Card

Company nAme and logo. Calvin Ostrow Co-Founder / Project Manager Office # 416-555-0193 Cell # 416-555-0147 VERIDAX.CA Calvin@veridax.ca

Font styles to use
Other font styles liked:
• Modern

Requirements
Must have
• Company name and logo, contact info, using the black, gold and white color scheme.

```html
<!DOCTYPE html>
<html lang="en">
<head>
<meta charset="utf-8">
<title>VERIDAX Business Card</title>
<link rel="stylesheet" href="https://fonts.googleapis.com/css2?family=Poppins:wght@300;400;500&display=swap">
<style>
  :root {
    --stage: #1c1c1c;
    --card-dark: #2f2f2f;
    --card-light: #ffffff;
    --ink: #1f1f1f;
    --gold: #a8925e;
    --grey: #8a8a8a;
  }
  * { margin: 0; padding: 0; box-sizing: border-box; }
  html, body {
    width: 1200px; height: 880px; overflow: hidden;
    background: var(--stage);
    font-family: "Poppins", sans-serif;
  }
  .stage {
    position: relative; width: 1200px; height: 880px;
    display: flex; flex-direction: column; align-items: center; justify-content: center; gap: 44px;
  }
  .card {
    position: relative; width: 620px; height: 354px; border-radius: 22px;
    box-shadow: 0 14px 34px rgba(0,0,0,.55);
    overflow: hidden;
  }
  .card--back { background: var(--card-dark); }
  .card--front { background: var(--card-light); }

  .brand {
    position: absolute; display: flex; align-items: center; gap: 14px;
    font-weight: 300; letter-spacing: 8px; font-size: 40px; line-height: 1;
  }
  .brand__mark { width: 14px; height: 14px; background: var(--gold); }
  .card--back .brand { left: 50px; bottom: 62px; color: #ffffff; }
  .card--front .brand { left: 42px; top: 158px; color: var(--ink); font-size: 36px; letter-spacing: 7px; }

  .divider {
    position: absolute; left: 318px; top: 90px; width: 1px; height: 180px; background: var(--gold);
  }
  .contact { position: absolute; left: 348px; top: 86px; color: var(--ink); }
  .contact__name { font-size: 24px; font-weight: 400; letter-spacing: .5px; line-height: 1.1; }
  .contact__name .surname { color: var(--gold); }
  .contact__role { font-size: 13px; font-weight: 300; color: var(--grey); margin-top: 4px; }
  .contact__list { list-style: none; margin-top: 26px; font-size: 14px; font-weight: 400; }
  .contact__list li { display: flex; align-items: center; gap: 12px; height: 26px; }
  .contact__list svg { width: 14px; height: 14px; flex: none; }
  .contact__list .accent { color: var(--gold); }
</style>
</head>
<body>
<main class="stage">
  <section class="card card--back" aria-label="Card back">
    <div class="brand"><span class="brand__mark"></span>VERIDAX</div>
  </section>

  <section class="card card--front" aria-label="Card front">
    <div class="brand"><span class="brand__mark"></span>VERIDAX</div>
    <div class="divider"></div>
    <div class="contact">
      <p class="contact__name">CALVIN <span class="surname">OSTROW</span></p>
      <p class="contact__role">Co-Founder / Project Manager</p>
      <ul class="contact__list">
        <li>
          <svg viewBox="0 0 16 16"><path fill="#a8925e" d="M3 2h3l1 4-2 1c1 2 2 3 4 4l1-2 4 1v3c0 1-1 1-1 1C7 14 2 9 2 3c0 0 0-1 1-1z"/></svg>
          416-555-0193
        </li>
        <li>
          <svg viewBox="0 0 16 16"><rect x="4" y="1.5" width="8" height="13" rx="1.5" fill="none" stroke="#a8925e" stroke-width="1.4"/></svg>
          416-555-0147
        </li>
        <li>
          <svg viewBox="0 0 16 16"><circle cx="8" cy="8" r="6.3" fill="none" stroke="#a8925e" stroke-width="1.3"/><path d="M1.7 8h12.6M8 1.7c-3 3.5-3 9 0 12.6M8 1.7c3 3.5 3 9 0 12.6" fill="none" stroke="#a8925e" stroke-width="1"/></svg>
          <span>VERI<span class="accent">DAX</span>.CA</span>
        </li>
        <li>
          <svg viewBox="0 0 16 16"><rect x="1.5" y="3.5" width="13" height="9" fill="#a8925e"/><path d="M1.5 3.5 8 9l6.5-5.5" fill="none" stroke="#fff" stroke-width="1"/></svg>
          Calvin@veridax.ca
        </li>
      </ul>
    </div>
  </section>
</main>
</body>
</html>
```